Gestaltung einer Anzeige für eine Stelle als Triebfahrzeugführer
Ging alles sehr schnell und unkompliziert. Kommunikation verlief problemlos und auch zügig. Es wurde verstanden und umgesetzt was wir suchen. Wenn doch nur alles so einfach wäre. Danke für die Arbeit. Jetzt machen wir einen sehr professionellen Eindruck!
Zielgruppe
Wir sind ein privates Zugunternehmen und suchen Triebfahrzeugführer. Unsere Zielgruppe sind also Triebfahrzeugführer.
Aufgabenstellung
https://www.lorvank.example/
Bitte unter anderem unsere Bilder nehmen. Wir können weitere nachreichen. Unter dem Link sind Bilder unserer eigene Webseite zb. Für LUP Cargo. Sie dürfen aber natürlich auch Bilder von einem Mann vor Gleisen etc. verwenden

```html
<!DOCTYPE html>
<html lang="de">
<head>
<meta charset="utf-8">
<title>Stellenanzeige Triebfahrzeugführer – Lorvank Eisenbahn GmbH</title>
<link rel="stylesheet" href="https://fonts.googleapis.com/css2?family=Nunito+Sans:wght@400;700;800&family=Permanent+Marker&display=swap">
<style>
  :root {
    --red: #e30613;
    --ink: #1d1d1b;
    --panel-top: #f3f3f3;
    --panel-bottom: #e4e4e4;
    --white: #ffffff;
    --photo-sky: #c9d3dc;
    --photo-roof: #a5513d;
    --photo-train: #c92a2e;
    --photo-ground: #8a8276;
  }
  * { margin: 0; padding: 0; box-sizing: border-box; }
  html, body { width: 849px; height: 1200px; overflow: hidden; background: var(--white); }
  body { font-family: "Nunito Sans", Arial, sans-serif; color: var(--ink); }
  .ad { position: relative; width: 849px; height: 1200px; overflow: hidden; background: var(--white); }

  .side-panel {
    position: absolute; left: 558px; top: 0; width: 291px; height: 1200px;
    background: linear-gradient(180deg, var(--panel-top), var(--panel-bottom));
  }

  .headline-bubble { position: absolute; left: 95px; top: 18px; width: 380px; height: 185px; }
  .headline-bubble svg { position: absolute; inset: 0; }
  .headline-text {
    position: absolute; left: 0; top: 38px; width: 380px; text-align: center;
    font-family: "Permanent Marker", "Comic Sans MS", cursive;
    font-size: 36px; line-height: 46px; color: var(--ink); transform: rotate(-2deg);
  }

  .intro { position: absolute; left: 30px; top: 218px; width: 496px; text-align: center; font-size: 16.5px; line-height: 20.5px; }
  .job-title { color: var(--red); font-weight: 800; font-size: 25.5px; line-height: 31px; margin: 4px 0 6px; }

  .company-text { position: absolute; left: 51px; top: 399px; width: 480px; font-size: 14px; line-height: 20px; }
  .company-text b { font-weight: 800; }

  .cta-title { position: absolute; left: 51px; top: 518px; color: var(--red); font-weight: 800; font-size: 25.5px; }
  .cta-text { position: absolute; left: 51px; top: 569px; width: 490px; font-size: 14px; line-height: 20px; }
  .documents-intro { position: absolute; left: 51px; top: 663px; font-size: 14px; }

  .documents { position: absolute; left: 51px; top: 687px; width: 500px; list-style: none; font-size: 14px; line-height: 17.3px; }
  .documents li { position: relative; padding-left: 18px; margin-bottom: 7.3px; }
  .documents li::before { content: "•"; position: absolute; left: 0; }
  .documents .strong { font-weight: 800; }

  .photo {
    position: absolute; left: 0; top: 860px; width: 558px; height: 340px;
    background:
      linear-gradient(180deg, transparent 0 70%, var(--photo-ground) 100%),
      linear-gradient(105deg, var(--photo-roof) 0 22%, transparent 22%),
      linear-gradient(90deg, transparent 0 8%, var(--photo-train) 8% 72%, transparent 72%),
      linear-gradient(180deg, var(--photo-sky), #aeb8a0);
  }

  .info-block { position: absolute; left: 588px; width: 245px; }
  .info-title { color: var(--red); font-weight: 800; font-size: 16.5px; margin-bottom: 14px; }
  .info-list { list-style: none; font-size: 14px; line-height: 17.3px; }
  .info-list li { position: relative; padding-left: 17px; margin-bottom: 7.3px; }
  .info-list li::before { content: "•"; position: absolute; left: 0; }
  .tasks { top: 38px; }
  .requirements { top: 386px; }
  .offer { top: 704px; }

  .brand-box {
    position: absolute; left: 586px; top: 998px; width: 197px; height: 62px;
    background: var(--white); display: flex; align-items: center; justify-content: center; gap: 8px;
  }
  .brand-square { width: 16px; height: 16px; background: var(--red); }
  .brand-name { font-weight: 800; font-size: 14.5px; color: var(--red); }

  .contact { position: absolute; left: 589px; top: 1075px; font-size: 14px; line-height: 17.3px; }
  .contact strong { font-weight: 800; font-size: 14.5px; }
</style>
</head>
<body>
<main class="ad">
  <div class="side-panel"></div>

  <div class="headline-bubble">
    <svg width="380" height="185" viewBox="0 0 380 185" aria-hidden="true">
      <path d="M190 6 C300 6 372 45 372 88 C372 138 290 170 190 170 C150 170 118 165 90 156 L28 178 L55 140 C22 124 8 106 8 88 C8 45 80 6 190 6 Z"
            fill="#fff" stroke="#e30613" stroke-width="5" stroke-linejoin="round"/>
      <path d="M190 14 C292 14 362 50 362 88 C362 132 285 162 190 162 C150 162 120 157 92 148 L48 164 L66 136 C32 122 18 106 18 88 C18 50 88 14 190 14 Z"
            fill="none" stroke="#e30613" stroke-width="2"/>
    </svg>
    <div class="headline-text">„Nächster Halt:<br>Festanstellung!“</div>
  </div>

  <section class="intro">
    <p>Als Folge unseres Wachstums suchen wir Verstärkung<br>für unser Team in Form von</p>
    <h1 class="job-title">Triebfahrzeugführern (m/w/d) und<br>Rangierbegleitern (m/w/d)</h1>
    <p>für folgende Dienstorte:<br>Stendal, Ankum, Aschersleben, Schwerte</p>
  </section>

  <p class="company-text">Die Lorvank Eisenbahn GmbH ist ein privates Bahnunternehmen aus Talbrück und setzt sich aus dem Heideland Express, der LUP Cargo, der Lorvank Express und dem Lorvank Service zusammen. Seit <b>2016/2017</b> sind wir in <b>Niedersachsen/---</b> unterwegs und bedienen ein umfangreicheas Spektrum an Aufgaben.</p>

  <h2 class="cta-title">Haben wir Ihr Interesse geweckt?</h2>
  <p class="cta-text">Möchten Sie Teil eines dynamischen Teams werden und uns bei den sich aktiv ins Geschehen miteinbringen? Dann freuen wir uns auf Ihre Bewerbung, mit der Angabe Ihres frühmöglichen Eintrittstermins, welche Sie uns bitte per Post oder E-Mail an info@lorvank.example zusenden.</p>

  <p class="documents-intro">Bitte fügen Sie Ihrer Bewerbung folgende Unterlagen bei:</p>
  <ul class="documents">
    <li>Nachweis Ihres Triebfahrzeugführerscheins</li>
    <li>Nachweise des regelmäßigen Dienst- oder Fortbildungsunterrichts</li>
    <li class="strong">Bescheinigung über abgelegte Prüfungen der infrastrukturbezogenen (V-DB, BRW,PZB) und fahrzeugbezogenen (Baureihen)</li>
    <li>Vorhandene Fachkenntnisse</li>
    <li>falls vorhanden: Bescheinigung über abgelegte Tauglichkeitsuntersuchungen</li>
  </ul>

  <div class="photo" role="img" aria-label="Foto: roter Regionalzug mit Steuerwagen an einem Bahnsteig, dahinter Ziegeldächer, Bäume und ein Kirchturm"></div>

  <section class="info-block tasks">
    <h3 class="info-title">Aufgaben</h3>
    <ul class="info-list">
      <li>Zuverlässige und pünktliche Beförderung der Fahrgäste im Personennahverkehr</li>
      <li>Verantwortungsbewusster und sicherer Transport im Güterverkehr</li>
      <li>Beförderung eigener Fahrgäste im Touristikverkehr</li>
      <li>Eigenständiges Erkennen und Beheben von Störungen</li>
      <li>Durchführung von Vorbereitungs- und Abschlussdiensten</li>
      <li>Bei Interesse Mitwirkung in unserer Werkstatt zwecks Instandhaltung</li>
    </ul>
  </section>

  <section class="info-block requirements">
    <h3 class="info-title">Voraussetzungen</h3>
    <ul class="info-list">
      <li>Eisenbahnfahrzeugführerschein der Klasse B gemäß TfV</li>
      <li>Idealerweise erste Erfahrung als Triebfahrzeugführer oder Rangierbegleiter</li>
      <li>Gesundheitliche und psychologische Eignung</li>
      <li>Hohes Maß an Kunden- und Serviceorientierung</li>
      <li>Flexibilität und Zuverlässigkeit</li>
      <li>Bereitschaft zu Schicht- und Wechseldiensten</li>
    </ul>
  </section>

  <section class="info-block offer">
    <h3 class="info-title">Unser Angebot</h3>
    <ul class="info-list">
      <li>Vielseitige und abwechslungsreiche Tätigkeiten in einem wachsenden Eisenbahnverkehrsunternehmen</li>
      <li>Mitwirkungsrecht bei der Dienstgestaltung</li>
      <li>Einen sicheren Arbeitsplatz</li>
      <li>Leistungsgerechte und attraktive Vergütung mit Schichtzulagen</li>
      <li>Die Mitarbeit in einem motivierten und engagierten Team</li>
    </ul>
  </section>

  <div class="brand-box">
    <span class="brand-square"></span>
    <span class="brand-name">Lorvank Eisenbahn GmbH</span>
  </div>

  <address class="contact" style="font-style: normal;">
    <strong>Lorvank Eisenbahn GmbH</strong><br>
    Personalabteilung<br>
    Birkenweg 14<br>
    12345 Talbrück<br>
    info@lorvank.example
  </address>
</main>
</body>
</html>
```